Automotive spring company needs banner for website

Banner dimensions: 3840 x 880 pixels
Banner need to be consistent with our branding (logo, stationary, colors, fonts, message).
People images should show happiness and it is preferable those people are in or around a car unless it ties into one of the 3 quotes in the must haves below.
Use color blue #4885ed
and gold color #f7d105
Minimal, strong, clean, & tech

Target Market(s)

35-55 male and female

Industry/Entity Type

Auto Repair

Requirements
Must have
• Clickable element for "Shop" or "Make an Appointment"
• "25 Years of Customer Satisfaction" or
• "Get it Done Right by Specialist" or
• "Peace of Mind National Warranty"
• Use our font, Eurostile and/or complimentary font paring

```html
<!DOCTYPE html>
<html lang="en">
<head>
<meta charset="UTF-8">
<title>Coilwell – Peace of Mind National Warranty</title>
<link rel="stylesheet" href="https://fonts.googleapis.com/css2?family=Michroma&family=Archivo:wght@700;800&display=swap">
<style>
  :root {
    --cream-light: #fbf3e4;
    --cream: #f6e9d2;
    --cream-warm: #f1dcb8;
    --ink: #333333;
    --brand-gold: #d8b21a;
    --brand-blue: #4885ed;
    --button-top: #4a8af0;
    --button-bottom: #1f5cc8;
    --white: #ffffff;
  }

  * { margin: 0; padding: 0; box-sizing: border-box; }

  html, body {
    width: 1200px;
    height: 275px;
    overflow: hidden;
    background: var(--cream-light);
  }

  .banner {
    position: relative;
    width: 1200px;
    height: 275px;
    overflow: hidden;
    background: linear-gradient(90deg, var(--cream-warm) 0%, var(--cream) 45%, var(--cream-light) 100%);
  }

  .hero-photo {
    position: absolute;
    left: 0;
    top: 0;
    width: 600px;
    height: 270px;
    background:
      linear-gradient(180deg, rgba(255,255,255,0) 62%, rgba(214,214,210,0.85) 78%, rgba(236,236,232,0.9) 100%),
      radial-gradient(ellipse 120px 150px at 290px 130px, #f5c71f 0%, #f1c21e 55%, rgba(241,194,30,0) 100%),
      linear-gradient(180deg, #f3e6c8 0%, #e9d8a8 55%, #cfc6a0 75%, #c9c4b4 100%);
    -webkit-mask-image: linear-gradient(90deg, #000 0%, #000 70%, transparent 100%);
            mask-image: linear-gradient(90deg, #000 0%, #000 70%, transparent 100%);
  }

  .brand {
    position: absolute;
    right: 66px;
    top: 20px;
    display: flex;
    align-items: center;
    gap: 8px;
  }

  .brand-mark {
    width: 12px;
    height: 12px;
    background: var(--brand-gold);
  }

  .brand-name {
    font-family: "Michroma", sans-serif;
    font-size: 24px;
    letter-spacing: 1px;
    color: var(--brand-gold);
    line-height: 1;
  }

  .headline {
    position: absolute;
    right: 66px;
    top: 90px;
    text-align: right;
    font-family: "Michroma", sans-serif;
    font-size: 33px;
    line-height: 48px;
    color: var(--ink);
    letter-spacing: 0.5px;
    white-space: nowrap;
  }

  .headline span { display: block; }

  .shop-button {
    position: absolute;
    left: 982px;
    top: 210px;
    width: 152px;
    height: 44px;
    display: flex;
    align-items: center;
    justify-content: center;
    border-radius: 3px;
    background: linear-gradient(180deg, var(--button-top) 0%, var(--button-bottom) 100%);
    box-shadow: 0 1px 3px rgba(0,0,0,0.25);
    color: var(--white);
    font-family: "Archivo", sans-serif;
    font-weight: 800;
    font-size: 16px;
    letter-spacing: 0.5px;
    text-decoration: none;
  }

  .accent-rule {
    position: absolute;
    left: 0;
    bottom: 0;
    width: 1200px;
    height: 5px;
    background: var(--brand-blue);
  }
</style>
</head>
<body>
  <div class="banner">
    <div class="hero-photo" role="img" aria-label="Happy woman in a yellow shirt standing in a white convertible car with her arms spread wide"></div>

    <div class="brand">
      <span class="brand-mark"></span>
      <span class="brand-name">COILWELL</span>
    </div>

    <h1 class="headline">
      <span>PEACE OF MIND</span>
      <span>NATIONAL WARRANTY</span>
    </h1>

    <a class="shop-button" href="#shop">SHOP NOW</a>

    <div class="accent-rule"></div>
  </div>
</body>
</html>
```